Business Card Design Project

We need a business card to reflect the design of our website - just so it all ties in - it has a retro feel and can be found at http://www.velorasoulpair.com
We will need our phone 0437 215 964
Web address, and email velorapair@fernmail.com included
Our catch cry is "Classic Cocktail Music"
Perfect Live Music for Private & Corporate Events, Weddings and Dinner Music
Our names should be included :-
Maribel Thorne / piano & Dennis Holloway / bass
I am now also including our logo so that it can be included (in part or whole) somehow in the design
My partner thinks we should include our logo in some form in the design of the card - i will attach this here for you. I will attach eps but if you prefer another format please let me know
Regards
Mari

```html
<!DOCTYPE html>
<html lang="en">
<head>
<meta charset="utf-8">
<title>Velora Duo – Business Card</title>
<link rel="stylesheet" href="https://fonts.googleapis.com/css2?family=Big+Shoulders+Display:wght@500;600;700&display=swap">
<style>
  :root {
    --backdrop: #e7e3dc;
    --cream: #f4ebd6;
    --cream-text: #efe3c3;
    --charcoal: #4b4b4b;
    --card-dark: #4d4d4d;
    --coral: #e0613f;
    --coral-dark: #b9492c;
  }
  * { margin: 0; padding: 0; box-sizing: border-box; }
  html, body { width: 1200px; height: 1000px; overflow: hidden; }
  body {
    background: var(--backdrop);
    font-family: "Big Shoulders Display", "Arial Narrow", sans-serif;
    position: relative;
  }

  /* Front of card */
  .card-front {
    position: absolute; left: 140px; top: 115px;
    width: 625px; height: 378px;
    background: var(--cream);
    box-shadow: 0 2px 6px rgba(0,0,0,.18);
  }
  .duo-name {
    position: absolute; left: 0; right: 0; top: 102px;
    text-align: center; font-weight: 600; font-size: 50px;
    letter-spacing: 1px; color: var(--charcoal); line-height: 1;
    padding-left: 10px;
  }
  .ribbon { position: absolute; left: 88px; top: 166px; width: 400px; height: 58px; }
  .tagline {
    position: absolute; left: 88px; top: 170px; width: 400px;
    text-align: center; font-weight: 600; font-size: 33px;
    color: var(--cream-text); letter-spacing: .5px; line-height: 44px;
  }
  .member { position: absolute; top: 240px; text-align: center; line-height: 1; }
  .member--piano { left: 85px; width: 210px; }
  .member--bass { left: 338px; width: 200px; }
  .member-name { font-weight: 700; font-size: 32px; color: var(--charcoal); letter-spacing: .5px; }
  .member-role { font-weight: 700; font-size: 27px; color: var(--coral); margin-top: 4px; }

  /* Brand tile */
  .brand-tile {
    position: absolute; left: 1054px; top: 162px; width: 146px; height: 155px;
    background: var(--coral);
    display: flex; align-items: center; justify-content: center;
    font-weight: 600; font-size: 26px; color: var(--cream-text); text-align: center; line-height: 1;
  }

  /* Back of card */
  .card-back {
    position: absolute; left: 428px; top: 516px;
    width: 628px; height: 380px;
    background: var(--card-dark);
    color: var(--cream-text);
    text-align: center;
  }
  .back-brand {
    position: absolute; left: 0; right: 0; top: 48px;
    display: flex; align-items: center; justify-content: center; gap: 14px;
    font-weight: 600; font-size: 38px; line-height: 1;
  }
  .back-brand .dot {
    width: 34px; height: 34px; border-radius: 50%;
    border: 3px solid var(--cream-text);
  }
  .services {
    position: absolute; left: 0; right: 0; top: 174px;
    font-weight: 700; font-size: 27px; line-height: 40px; letter-spacing: .5px;
  }
  .divider {
    position: absolute; left: 127px; width: 356px; top: 266px;
    border-top: 2px dashed var(--coral);
  }
  .phone {
    position: absolute; left: 0; right: 0; top: 282px;
    font-weight: 700; font-size: 29px; letter-spacing: 1px;
  }
  .links {
    position: absolute; left: 0; right: 0; top: 325px;
    display: flex; justify-content: center; gap: 32px;
    font-weight: 700; font-size: 28px; letter-spacing: .5px;
  }
</style>
</head>
<body>

  <section class="card-front">
    <h1 class="duo-name">VELORA DUO</h1>
    <svg class="ribbon" viewBox="0 0 400 58" aria-hidden="true">
      <polygon points="0,14 48,14 48,56 0,56 14,35" fill="var(--coral)"/>
      <polygon points="400,14 352,14 352,56 400,56 386,35" fill="var(--coral)"/>
      <polygon points="48,48 48,56 60,48" fill="var(--coral-dark)"/>
      <polygon points="352,48 352,56 340,48" fill="var(--coral-dark)"/>
      <rect x="48" y="4" width="304" height="44" fill="var(--coral)"/>
    </svg>
    <p class="tagline">CLASSIC COCKTAIL MUSIC</p>
    <div class="member member--piano">
      <p class="member-name">MARIBEL THORNE</p>
      <p class="member-role">PIANO</p>
    </div>
    <div class="member member--bass">
      <p class="member-name">DENNIS HOLLOWAY</p>
      <p class="member-role">BASS</p>
    </div>
  </section>

  <div class="brand-tile">VELORA<br>DUO</div>

  <section class="card-back">
    <div class="back-brand"><span class="dot"></span><span>VELORA DUO</span></div>
    <p class="services">PERFECT LIVE MUSIC FOR PRIVATE &amp; CORPORATE EVENTS<br>WEDDINGS AND DINNER MUSIC</p>
    <div class="divider"></div>
    <p class="phone">0437 215 964</p>
    <p class="links"><span>WWW.VELORASOULPAIR.COM</span><span>VELORAPAIR@FERNMAIL.COM</span></p>
  </section>

</body>
</html>
```